Electronics Recycling and IT Asset Disposition Flyer and Brochure Design

We need a 2 side A5 Flyer and 4 side A4 folder( brochure) for our electronics waste recycling and IT asset management and disposition business.
Our business provides free electronics waste recycling for companies, schools, learning institutions,councils, IT companies and government sectors. Many people are ignorant of responsible recycling of electronics which could harm our health if not treated properly.
The list of other services attached in the pdf.
We provide an end to end and tailored solution for our customers from collection, logistics, data sanitisation, remarketing and recycling.

The Flyer should create awareness of responsible electronics recycling and drive the audience to contact us or go to our website to learn more about the company and services.A brief list of services should also be included in the flyer.The goal is to get the audience to contact us to enquire more about our services.

The Brochure should include all the above plus provide more details about the company, processes, services,contact details (fb, linkedin,Twitter). The goal is to convert the audience to customers for recycling and provide other services as added services.

The final design for both flyer and brochure should communicate responsible recycling of electronic scrap and tailored solution for every organisation.

The company website is www.kelvora-scrap.com.au based in Australia. We serve clients nationwide.

Target Market(s)

IT companies, Corporate, schools and learning institutions, government sector

Industry/Entity Type

Recycling

Contact Information for Business Card

Name: Derek Ollinfeld
email: derek@kelvora-scrap.com.au
website: www.kelvora-scrap.com.au
mobile: +614 631 02957
Phone: 1300 64 2835

Font styles to use
Serif

Requirements
Must have
• I would like the designs to have more images and icons
Nice to have
Should not have
• none

```html
<!DOCTYPE html>
<html lang="en">
<head>
<meta charset="utf-8">
<title>Kelvora Scrap – Flyer</title>
<link href="https://fonts.googleapis.com/css2?family=Ubuntu:wght@400;500;700&family=Source+Sans+3:wght@400;600&display=swap" rel="stylesheet">
<style>
:root{
  --green:#3f9a2e;
  --green-dark:#1f7a2a;
  --green-light:#6cbf3f;
  --ink:#222;
  --text:#333;
  --grey-bg:#ececec;
  --stage:#e6e2dc;
  --white:#fff;
}
*{margin:0;padding:0;box-sizing:border-box}
html,body{width:1200px;height:904px;overflow:hidden;background:var(--stage)}
body{position:relative;font-family:"Source Sans 3",Arial,sans-serif;color:var(--text)}
.page{position:absolute;top:107px;width:534px;height:692px;background:var(--grey-bg);overflow:hidden;box-shadow:0 3px 10px rgba(0,0,0,.25)}
.page--front{left:48px}
.page--back{left:616px}
.page-art{position:absolute;inset:0}
.abs{position:absolute}
h1,h2{font-weight:500}

/* front */
.brand{position:absolute;left:40px;top:38px;display:flex;align-items:center;gap:6px;font-family:"Ubuntu",sans-serif;font-weight:700;font-size:25px;color:var(--green)}
.brand-dot{width:12px;height:12px;border-radius:50%;background:var(--green)}
.headline{left:19px;top:354px;width:240px;font-family:"Ubuntu",sans-serif;font-weight:500;font-size:22px;line-height:29px;color:var(--ink);letter-spacing:-.3px;white-space:nowrap;z-index:2}
.headline .big{font-weight:700;font-size:27px;letter-spacing:-.5px}
.headline em{font-style:normal;color:var(--green)}
.tab{position:absolute;height:18px;padding:0 22px;font-family:"Ubuntu",sans-serif;font-weight:500;font-size:15px;line-height:18px;color:var(--white);white-space:nowrap;clip-path:polygon(0 0,100% 0,calc(100% - 12px) 100%,0 100%)}
.tab--provides{left:0;top:453px;width:155px;background:var(--green)}
.tab--about{left:260px;top:360px;width:122px;background:var(--ink);padding-left:24px;height:20px;line-height:21px}
.body-copy{font-size:8.2px;line-height:11.4px;text-align:justify}
.provides-copy{left:23px;top:478px;width:229px}
.provides-copy p+p{margin-top:6px}
.provides-list{left:24px;top:573px;width:200px;list-style:none;display:grid;grid-template-columns:100px 100px;row-gap:6px;font-size:8.4px}
.provides-list li{position:relative;padding-left:13px}
.provides-list li::before,.bullets li::before{content:"";position:absolute;left:0;top:3px;width:4.5px;height:4.5px;border-radius:50%;background:var(--green-dark)}
.about-block{left:266px;top:361px;width:268px;height:276px;background:var(--green-dark)}
.about-copy{left:283px;top:386px;width:234px;color:var(--white);font-size:7.6px;line-height:10.4px}
.about-copy p+p{margin-top:10px}
.footer-contacts{top:648px;font-size:8.6px;color:var(--white);line-height:18px;white-space:nowrap}
.footer-contacts .row{display:flex;align-items:center;gap:5px}
.key{display:inline-flex;width:11px;height:11px;border-radius:50%;background:var(--ink);color:var(--white);font-size:7px;font-weight:600;align-items:center;justify-content:center}
.footer-contacts--left{right:290px;text-align:right}
.footer-contacts--left .row{justify-content:flex-end}
.footer-contacts--right{left:283px}
.footer-divider{left:266px;top:650px;width:1px;height:30px;background:var(--white)}

/* back */
.title-tab{left:114px;top:0;width:296px;height:54px;background:var(--green-dark);border-radius:0 0 6px 6px;font-family:"Ubuntu",sans-serif;font-weight:500;font-size:29px;color:var(--white);text-align:center;line-height:60px}
.service-head{position:absolute;left:0;display:flex;align-items:center}
.tick{width:24px;height:18px;background:var(--ink);display:flex;align-items:center;justify-content:center}
.service-head .tab{position:relative;padding:0 20px 0 7px;font-size:11.2px;height:18px;line-height:18px;background:var(--green)}
.bullets{list-style:none;font-size:8.3px;line-height:11.4px;color:var(--text)}
.bullets li{position:relative;padding-left:11px}
.bullets li+li{margin-top:6px}
.sub{padding-left:26px;font-size:8.3px;line-height:14.3px}
.quote-band{left:0;top:562px;width:335px;height:32px;background:var(--green-dark);color:var(--white);font-size:8.3px;line-height:11.4px;padding:4px 8px 0 18px}
.quote-name{left:18px;top:598px;font-size:10.4px;color:var(--ink)}
.quote-role{left:18px;top:615px;font-size:7.3px;color:var(--ink)}
</style>
</head>
<body>

<section class="page page--front">
  <svg class="page-art" viewBox="0 0 534 692" width="534" height="692">
    <defs>
      <linearGradient id="beach" x1="0" y1="0" x2="0" y2="1">
        <stop offset="0" stop-color="#d7e8f3"/>
        <stop offset=".42" stop-color="#9fc3d6"/>
        <stop offset=".62" stop-color="#6f9fb8"/>
        <stop offset=".78" stop-color="#d9c7a8"/>
        <stop offset="1" stop-color="#c9b28e"/>
      </linearGradient>
      <linearGradient id="swoosh" x1="0" y1="0" x2="1" y2="0">
        <stop offset="0" stop-color="#1f7a2a"/>
        <stop offset="1" stop-color="#6cbf3f"/>
      </linearGradient>
    </defs>
    <rect x="0" y="0" width="534" height="340" fill="url(#beach)" role="img" aria-label="Photo of a smiling family walking hand in hand along a sunny beach"/>
    <path d="M0 0H264C222 70 124 96 0 92Z" fill="var(--white)"/>
    <path d="M0 92C124 96 212 66 252 14C208 86 116 118 0 122Z" fill="url(#swoosh)"/>
    <path d="M0 200C90 300 260 342 534 300V692H0Z" fill="var(--grey-bg)"/>
    <path d="M0 200C90 300 260 342 534 300V316C300 364 110 330 0 262Z" fill="url(#swoosh)"/>
    <path d="M0 262C110 330 300 364 534 316V322C300 372 110 340 0 272Z" fill="var(--white)"/>
    <path d="M0 640C180 616 360 614 534 634V692H0Z" fill="var(--green)"/>
    <path d="M0 636C180 612 360 610 534 630" fill="none" stroke="var(--white)" stroke-width="2"/>
  </svg>

  <div class="brand"><span>Kelvora</span><span class="brand-dot"></span></div>

  <div class="about-block abs"></div>

  <h1 class="abs headline">
    <span class="big"><em>BE</em> RESPONSIBLE</span><br>
    <em>TODAY</em> FOR A BETTER<br>
    <em>FUTURE</em> TOMORROW
  </h1>

  <h2 class="tab tab--about">ABOUT US</h2>
  <div class="abs about-copy body-copy">
    <p>Kelvora Scrap is a full service IT asset disposition, electronics waste recycling and electronics scrap purchasing company in Australia. Our vision is to become an industry leader by building genuine relationships with clients based on integrity, service quality and consistency, as well as maximizing value recovery.</p>
    <p>Our focus is to reduce electronic waste generation through creating awareness in organisations and community about the importance of responsible recycling of electronics waste. Our goal is to provide end-to-end solution in e-waste management through established processes and technological innovations, drive higher returns for our customers and enhance conservation of raw metals within our ecosystem.</p>
    <p>Our team of dedicated engineers and professionals work with companies, government offices, institutions and SMEs across Australia to provide personalised IT asset disposal and e-waste management solutions to suit their needs. Our experience and knowledge in this industry will help us to understand and provide innovative solutions to manage your end of life IT assets. We aim at maximising returns and providing cost effective ways to ensure a positive impact on your bottom-line.</p>
  </div>

  <h2 class="tab tab--provides">WE PROVIDES</h2>
  <div class="abs provides-copy body-copy">
    <p>Our business provides free electronics waste recycling for companies, schools, learning institutions, councils, IT companies and government sectors. Many people are ignorant of responsible recycling of electronics which could harm our health if not treated properly.</p>
    <p>We provide an end to end and tailored solution for our customers from</p>
  </div>
  <ul class="abs provides-list">
    <li>Collection</li><li>Logistics</li>
    <li>Data sanitisation</li><li>Remarketing</li>
    <li>and Recycling</li>
  </ul>

  <div class="abs footer-contacts footer-contacts--left">
    <div class="row"><span class="key">T</span> : 1300 64 2835(tollfree)</div>
    <div class="row"><span class="key">E</span> : contact@kelvora-scrap.com.au</div>
  </div>
  <div class="abs footer-divider"></div>
  <div class="abs footer-contacts footer-contacts--right">
    <div class="row"><span class="key">W</span> : www.kelvora-scrap.com.au</div>
    <div class="row"><span class="key">A</span> : 18-22 Larchmont Road, Wyndale 2150 NSW</div>
  </div>
</section>

<section class="page page--back">
  <svg class="page-art" viewBox="0 0 534 692" width="534" height="692">
    <defs>
      <linearGradient id="scrap" x1="0" y1="0" x2="1" y2="1">
        <stop offset="0" stop-color="#f2f2f2"/>
        <stop offset=".5" stop-color="#d9d9d9"/>
        <stop offset="1" stop-color="#c9c9c9"/>
      </linearGradient>
      <linearGradient id="couple" x1="0" y1="0" x2="0" y2="1">
        <stop offset="0" stop-color="#e4e4e4"/>
        <stop offset=".5" stop-color="#b8d9a6"/>
        <stop offset="1" stop-color="#8fa7bf"/>
      </linearGradient>
    </defs>
    <rect width="534" height="692" fill="url(#scrap)" role="img" aria-label="Faint background photo of piled electronic waste"/>
    <rect x="312" y="477" width="222" height="164" fill="url(#couple)" role="img" aria-label="Photo of a happy couple sitting together"/>
    <path d="M0 640C180 616 360 614 534 634V692H0Z" fill="var(--green)"/>
    <path d="M0 636C180 612 360 610 534 630" fill="none" stroke="var(--white)" stroke-width="2"/>
  </svg>

  <h1 class="abs title-tab">SERVICE OFFERING</h1>

  <div class="service-head" style="top:72px"><span class="tick"><svg width="10" height="9" viewBox="0 0 10 9"><path d="M1 5l3 3 5-7" fill="none" stroke="#fff" stroke-width="2"/></svg></span><h2 class="tab">Secure E-Waste Collection Service</h2></div>
  <ul class="abs bullets" style="left:30px;top:102px;width:230px">
    <li>Kelvora Scrap collects electronic waste from schools, businesses, home users and government departments</li>
    <li>Registration of assets and reporting</li>
  </ul>
  <ul class="abs bullets" style="left:277px;top:102px;width:230px">
    <li>Secure collection includes pick up of e-waste and transportation to our recycling facility in a secured truck</li>
  </ul>

  <div class="service-head" style="top:153px"><span class="tick"><svg width="10" height="9" viewBox="0 0 10 9"><path d="M1 5l3 3 5-7" fill="none" stroke="#fff" stroke-width="2"/></svg></span><h2 class="tab">Receipting Registration, Test and Audit Services</h2></div>
  <ul class="abs bullets" style="left:30px;top:180px;width:230px">
    <li>Registering your assets on our Asset Management System</li>
    <li>Test, audit and verify specifications, condition and resale value</li>
  </ul>
  <ul class="abs bullets" style="left:277px;top:180px;width:230px">
    <li>Provide a detailed asset report</li>
    <li>Cleaning and removal of company logos and asset tags</li>
  </ul>

  <div class="service-head" style="top:230px"><span class="tick"><svg width="10" height="9" viewBox="0 0 10 9"><path d="M1 5l3 3 5-7" fill="none" stroke="#fff" stroke-width="2"/></svg></span><h2 class="tab">Certified Data Erasure Services</h2></div>
  <ul class="abs bullets" style="left:30px;top:258px;width:230px">
    <li>To provide secure data destruction:</li>
  </ul>
  <div class="abs sub" style="left:30px;top:269px">X1 pass<br>X3 pass (Recommended, DoD standard)<br>X7 pass</div>
  <ul class="abs bullets" style="left:277px;top:258px;width:230px">
    <li>Total destruction of HDDs by degaussing</li>
    <li>Total physical destruction of any storage media by shredding</li>
  </ul>

  <div class="service-head" style="top:314px"><span class="tick"><svg width="10" height="9" viewBox="0 0 10 9"><path d="M1 5l3 3 5-7" fill="none" stroke="#fff" stroke-width="2"/></svg></span><h2 class="tab">IT Asset Remarketing</h2></div>
  <ul class="abs bullets" style="left:30px;top:345px;width:480px">
    <li>Recover client’s IT asset and mobile devices for valuation and remarketing</li>
  </ul>

  <div class="service-head" style="top:361px"><span class="tick"><svg width="10" height="9" viewBox="0 0 10 9"><path d="M1 5l3 3 5-7" fill="none" stroke="#fff" stroke-width="2"/></svg></span><h2 class="tab">Processing &amp; recycling of electronic waste</h2></div>
  <ul class="abs bullets" style="left:30px;top:391px;width:480px">
    <li>All assets with no market value will be processed as E-Waste and recycled with zero to landfill in our ISO certified partner refinery overseas for metals recovery</li>
  </ul>

  <div class="service-head" style="top:418px"><span class="tick"><svg width="10" height="9" viewBox="0 0 10 9"><path d="M1 5l3 3 5-7" fill="none" stroke="#fff" stroke-width="2"/></svg></span><h2 class="tab">IT Services &amp; Data Center Setup, Relocation and Decommissioning</h2></div>
  <ul class="abs bullets" style="left:30px;top:446px;width:230px">
    <li>Deployment, relocation and decommissioning of IT systems by professional Northgate and Veltrix certified engineers</li>
    <li>IT Systems deployment and support for small and medium size business</li>
  </ul>
  <ul class="abs bullets" style="left:277px;top:446px;width:230px">
    <li>Data Center decommissioning/racking/de-racking and relocation</li>
  </ul>

  <div class="service-head" style="top:510px"><span class="tick"><svg width="10" height="9" viewBox="0 0 10 9"><path d="M1 5l3 3 5-7" fill="none" stroke="#fff" stroke-width="2"/></svg></span><h2 class="tab">IT Asset Auditing</h2></div>
  <ul class="abs bullets" style="left:33px;top:536px;width:280px">
    <li>Recording of Manufacturer and Model per asset (additionally HDD quantity and capacity for Server &amp; Storage assets)</li>
  </ul>

  <blockquote class="abs quote-band">“ Kelvora Scrap helped us to remove all our old equipment from our IT store room on a very short notice. Will be using their services again. ”</blockquote>
  <p class="abs quote-name">Marcus Delaney</p>
  <p class="abs quote-role">IT Infrastructure Manager</p>

  <div class="abs footer-contacts footer-contacts--left">
    <div class="row"><span class="key">T</span> : 1300 64 2835(tollfree)</div>
    <div class="row"><span class="key">E</span> : contact@kelvora-scrap.com.au</div>
  </div>
  <div class="abs footer-divider"></div>
  <div class="abs footer-contacts footer-contacts--right">
    <div class="row"><span class="key">W</span> : www.kelvora-scrap.com.au</div>
    <div class="row"><span class="key">A</span> : 18-22 Larchmont Road, Wyndale 2150 NSW</div>
  </div>
</section>

</body>
</html>
```